Mineral Drinking Water Label Design

We need a label design for a new bottled drinking water based in (either Pwani or Dar Es Salaam, decision is not yet finalized), Tanzania on the coast of East Africa.

We will use underground aquifers as our only source of raw water(pre treated water).

Which will then be treated through osmosis process, then the mineral water will be bottled in standard 500ml, 1000ml and 1500 ml plastic PET bottles for customer consumption.

We have a vision of expanding our supply network to cover the entire country. Therefore, we expect the label to communicate trust, purity, cleanliness, healthiness of water contained.

The uniqueness and attractiveness of the label/logo is of utmost importance.

With regards to water brand name, we prefer that you use your own imagination and creativity to come up with a name that might be more suited to your individual design.

Note: Different shades of blue are mainly associated with drinking water in Tanzania, however feel free to use any other colors.

Target Market(s)

Upper Class citizens, Hotels, Large Supermarkets etc

Font styles to use
Script

Colors

Designer to choose colors to be used in the design.

```html
<!DOCTYPE html>
<html lang="en">
<head>
<meta charset="utf-8">
<title>Maji Pwani Drinking Water Label</title>
<link rel="stylesheet" href="https://fonts.googleapis.com/css2?family=Almendra+Display&family=Questrial&family=Oswald:wght@500&display=swap">
<style>
  :root {
    --canvas-bg: #9b9b9b;
    --label-blue: #2766a8;
    --label-deep: #1c4f8a;
    --band-cyan: #3ec8ee;
    --glow-cyan: #7fe6f7;
    --ink-navy: #123f73;
    --white: #ffffff;
  }
  * { margin: 0; padding: 0; box-sizing: border-box; }
  html, body {
    width: 1200px;
    height: 1000px;
    overflow: hidden;
    background: var(--canvas-bg);
  }
  .canvas {
    position: relative;
    width: 1200px;
    height: 1000px;
  }
  .label {
    position: absolute;
    left: 282px;
    top: 50px;
    width: 636px;
    height: 900px;
    overflow: hidden;
    background:
      radial-gradient(ellipse 70% 42% at 50% 64%, var(--glow-cyan) 0%, #4fb6e4 30%, rgba(39,102,168,0) 75%),
      linear-gradient(180deg, var(--label-blue) 0%, #2d73b6 60%, var(--label-blue) 100%);
  }
  .purity-band {
    position: absolute;
    left: 0; right: 0;
    top: 41px;
    height: 34px;
    background: var(--band-cyan);
    color: var(--ink-navy);
    font-family: "Questrial", sans-serif;
    font-size: 22px;
    letter-spacing: 1px;
    text-align: center;
    line-height: 34px;
    white-space: nowrap;
  }
  .brand {
    position: absolute;
    left: 0; right: 0;
    top: 130px;
    display: flex;
    justify-content: center;
    align-items: center;
    gap: 14px;
    font-family: "Questrial", sans-serif;
    font-size: 58px;
    color: var(--white);
    white-space: nowrap;
  }
  .brand-dot {
    width: 22px;
    height: 22px;
    border-radius: 50%;
    background: var(--band-cyan);
  }
  .product-name {
    position: absolute;
    left: 0; right: 0;
    top: 290px;
    text-align: center;
    font-family: "Almendra Display", serif;
    font-weight: 400;
    font-size: 104px;
    line-height: 1;
    color: var(--white);
    white-space: nowrap;
  }
  .product-type {
    position: absolute;
    left: 0; right: 0;
    top: 470px;
    text-align: center;
    font-family: "Questrial", sans-serif;
    font-size: 54px;
    line-height: 70px;
    color: var(--ink-navy);
    white-space: nowrap;
  }
  .calorie-badge {
    position: absolute;
    left: 24px;
    top: 680px;
    width: 44px;
    height: 112px;
    background: var(--white);
    border-radius: 6px;
    color: var(--ink-navy);
    font-family: "Questrial", sans-serif;
    font-size: 10px;
    line-height: 1.1;
    text-align: center;
    padding-top: 8px;
  }
  .calorie-badge strong {
    display: block;
    font-size: 22px;
    margin-bottom: 4px;
  }
  .volume-band {
    position: absolute;
    left: 0; right: 0;
    bottom: 0;
    height: 72px;
    background: var(--label-deep);
    color: var(--white);
    font-family: "Oswald", sans-serif;
    font-weight: 500;
    font-size: 30px;
    text-align: center;
    line-height: 72px;
    letter-spacing: 1px;
    white-space: nowrap;
  }
</style>
</head>
<body>
  <div class="canvas">
    <div class="label">
      <div class="purity-band">100% PURE PACKAGED DRINKING WATER</div>
      <div class="brand"><span class="brand-dot"></span><span class="brand-name">coralis</span></div>
      <h1 class="product-name">Maji Pwani</h1>
      <p class="product-type">Packaged<br>Drinking Water</p>
      <div class="calorie-badge"><strong>0</strong>calories per serving</div>
      <div class="volume-band">1 Liter 33.8 FL OZ</div>
    </div>
  </div>
</body>
</html>
```